Corporate Design für Garten- und Landschaftsbau
Sehr guter Desinger, sehr schnelle Reaktion auf Änderungswünsche, alles bestens gelaufen, jederzeit gerne wieder, vorbildlich.
Zielgruppe
-Garten- und Landschaftsbau
-Bagger- und Erdarbeiten
-Kellertrockenlegung
-Hausmeisterdienste
-Individuelle Gartengestaltung
Aufgabenstellung
Eventuell ein Baggerarm mit Baggerlöffel und oder einen Baum oder ein Strauch

```html
<!DOCTYPE html>
<html lang="de">
<head>
<meta charset="utf-8">
<title>Brenner Corporate Design</title>
<link href="https://fonts.googleapis.com/css2?family=Lato:wght@400&family=Open+Sans:wght@400;600;700&display=swap" rel="stylesheet">
<style>
:root{
  --green:#0b7d3e;
  --ink:#1d1d1b;
  --line:#4a4a4a;
  --paper:#ffffff;
  --card-edge:#c8c8c8;
}
*{margin:0;padding:0;box-sizing:border-box}
html,body{width:785px;height:1200px;overflow:hidden;background:var(--paper)}
body{position:relative;font-family:"Open Sans",Arial,sans-serif;color:var(--ink)}
.abs{position:absolute}

.brand-name{font-family:"Open Sans",Arial,sans-serif;font-weight:600;color:var(--green);line-height:1;white-space:nowrap}
.brand-mark{display:inline-block;background:var(--green);border-radius:50%;flex:none}
.brand-tag{font-family:"Lato",Arial,sans-serif;font-weight:400;color:var(--ink);white-space:nowrap;text-transform:uppercase}

/* main logo */
.hero-logo{left:169px;top:92px;width:428px;display:flex;align-items:center;justify-content:center;gap:16px}
.hero-logo .brand-mark{width:40px;height:40px}
.hero-logo .brand-name{font-size:90px}
.hero-tag{left:0;width:785px;top:213px;text-align:center;font-size:14.5px;letter-spacing:0.22em}

/* letterhead */
.letterhead{left:157px;top:308px;width:468px;height:662px;border:1px solid var(--line)}
.lh-logo{left:288px;top:26px;width:152px;display:flex;align-items:center;justify-content:flex-end;gap:6px}
.lh-logo .brand-mark{width:12px;height:12px}
.lh-logo .brand-name{font-size:30px}
.lh-tag{left:288px;top:71px;width:152px;text-align:right;font-size:5.2px;letter-spacing:0.16em}
.services{list-style:none;font-size:7.6px;line-height:12.6px;font-weight:400;white-space:nowrap}
.services li{position:relative;padding-left:8px}
.services li::before{content:"";position:absolute;left:0;top:4.3px;width:4px;height:4px;background:var(--green)}
.lh-services{left:323px;top:105px}
.return-address{left:37px;top:133px;font-size:6.2px;color:#555}
.fold-mark{left:0;top:247px;width:24px;height:0;border-top:1px solid #999}
.lh-footer{top:602px;font-size:6px;line-height:8.5px;white-space:nowrap}
.f1{left:41px}.f2{left:163px}.f3{left:329px}

/* business cards */
.card{top:1033px;width:190px;height:123px;border:1px solid var(--card-edge);background:var(--paper);overflow:hidden}
.card-front{left:203px}
.card-back{left:410px}
.cf-logo{left:0;top:18px;width:190px;display:flex;align-items:center;justify-content:center;gap:5px}
.cf-logo .brand-mark{width:9px;height:9px}
.cf-logo .brand-name{font-size:23px}
.cf-tag{left:0;top:52px;width:190px;text-align:center;font-size:4.6px;letter-spacing:0.15em}
.cf-band{left:0;top:75px;width:190px;height:48px;background:var(--green);display:flex;gap:9px;padding:6px 0 0 10px}
.cf-band .services{color:#fff;font-size:5.2px;line-height:8.6px}
.cf-band .services li{padding-left:6px}
.cf-band .services li::before{background:#fff;width:3px;height:3px;top:2.8px}
.cb-name{left:21px;top:42px;font-size:8px;font-weight:700}
.contact{left:105px;display:flex;align-items:flex-start;gap:4px;font-size:5.3px;line-height:6.5px;white-space:nowrap}
.contact svg{flex:none}
.c1{top:43px}.c2{top:58px}.c3{top:71px}
.cb-rule{left:0;top:100px;width:190px;display:flex;align-items:center;gap:3px;font-size:5.3px;white-space:nowrap}
.cb-rule .bar{height:2px;background:var(--green)}
.cb-rule .bar.left{width:101px;flex:none}
.cb-rule .bar.right{flex:1}
</style>
</head>
<body>

<section class="abs hero-logo">
  <span class="brand-mark"></span>
  <span class="brand-name">Brenner</span>
</section>
<p class="abs brand-tag hero-tag">Garten und Landschaftsbau Brenner</p>

<section class="abs letterhead">
  <div class="abs lh-logo"><span class="brand-mark"></span><span class="brand-name">Brenner</span></div>
  <p class="abs brand-tag lh-tag">Garten und Landschaftsbau Brenner</p>

  <ul class="abs services lh-services">
    <li>Garten- und Landschaftspflege</li>
    <li>Bagger und Erdarbeiten</li>
    <li>Kellertrockenlegung</li>
    <li>Hausmeisterdieste</li>
    <li>Individuelle Gartengestaltung</li>
    <li>Tersassen</li>
    <li>Pflasterarbeiten</li>
    <li>Wegbesfestigung</li>
  </ul>

  <p class="abs return-address">Brenner&nbsp; Lindenweg 4 55620 Mühlbach</p>
  <span class="abs fold-mark"></span>

  <div class="abs lh-footer f1">Brenner<br>Garten- und Landschaftsbau Brenner<br>Lindenweg 4<br>55620 Mühlbach</div>
  <div class="abs lh-footer f2">Telefon: 0170 - 12 34 567<br>E-Mail: info@garten-landschaftsbau-brenner.de</div>
  <div class="abs lh-footer f3">Musterbank Mainz<br>IBAN: DE00 1234 5678 9000 1111 22<br>BIC: MUSTDEM1XXX</div>
</section>

<section class="abs card card-front">
  <div class="abs cf-logo"><span class="brand-mark"></span><span class="brand-name">Brenner</span></div>
  <p class="abs brand-tag cf-tag">Garten und Landschaftsbau Brenner</p>
  <div class="abs cf-band">
    <ul class="services">
      <li>Garten- und Landschaftspflege</li>
      <li>Bagger und Erdarbeiten</li>
      <li>Kellertrockenlegung</li>
      <li>Hausmeisterdieste</li>
    </ul>
    <ul class="services">
      <li>Individuelle Gartengestaltung</li>
      <li>Tersassen</li>
      <li>Pflasterarbeiten</li>
      <li>Wegbesfestigung</li>
    </ul>
  </div>
</section>

<section class="abs card card-back">
  <p class="abs cb-name">Max Muster</p>
  <div class="abs contact c1">
    <svg width="9" height="9" viewBox="0 0 10 10"><circle cx="5" cy="5" r="4.5" fill="none" stroke="#1d1d1b" stroke-width="0.6"/><path d="M3.3 2.8l1 1-.5.6c.3.7.9 1.3 1.6 1.6l.6-.5 1 1-.7.7C4.8 7 3 5.2 2.6 3.5z" fill="#1d1d1b"/></svg>
    <span>0170 - 12 34 567</span>
  </div>
  <div class="abs contact c2">
    <svg width="9" height="9" viewBox="0 0 10 10"><circle cx="5" cy="5" r="4.5" fill="none" stroke="#1d1d1b" stroke-width="0.6"/><text x="5" y="6.7" font-size="5" text-anchor="middle" font-family="Arial,sans-serif" fill="#1d1d1b">@</text></svg>
    <span>info@galabau-brenner.de</span>
  </div>
  <div class="abs contact c3">
    <svg width="9" height="9" viewBox="0 0 10 10"><circle cx="5" cy="5" r="4.5" fill="none" stroke="#1d1d1b" stroke-width="0.6"/><path d="M5 2.2a1.8 1.8 0 0 1 1.8 1.8C6.8 5.3 5 7.6 5 7.6S3.2 5.3 3.2 4A1.8 1.8 0 0 1 5 2.2z" fill="#1d1d1b"/><circle cx="5" cy="4" r=".6" fill="#fff"/></svg>
    <span>Lindenweg 4<br>55620 Mühlbach</span>
  </div>
  <div class="abs cb-rule"><span class="bar left"></span><span>www.galabau-brenner.de</span><span class="bar right"></span></div>
</section>

</body>
</html>
```